Flyer für Trauerredner
Vielen Dank an das Designer-Team von stonebrook! Sie würden nicht müde, auch die letzten Änderungswünsche umzusetzen und dies sehr professionell. Mein Kompliment und meine Empfehlung für künftige Projekte! Gern wieder! Beste Grüße Bernd Wallner
Zielgruppe
Ich starte in Kürze als (freier, nicht-kirchlicher) Trauerredner und werde individuelle Trauerfeiern organisieren und durchführen.
Später sollen evtl. Trauerbegleitung für Angehörige und Beratung bei der Bestattung und Bestattungsvorsorge hinzukommen.
Als Zielgruppe würde ich zunächst die Bestatter in meiner Umgebung (Berlin und Umland) sehen, nach und nach auch Direktanfragen von Privatpersonen, die mich bei einer Trauerfeier gehört haben.
Aufgabenstellung
Der Flyer sollte modern und relativ schlicht gestaltet sein, ohne kirchliche Symbole.
Bei den Maßen bin ich offen, als Maximum sehe ich DIN lang/quer, sodass dieser per Brief verschickt werden kann, ansonsten zum Mitnehmen für Trauergäste auf Trauerfeiern/Bestattungen.
Ich habe 'lichtwerk.berlin' als Webadresse reserviert. Dies soll künftig auch die Firmenbezeichnung sein. Eventuell könnte man einen QR-Code verwenden?
Später kommen noch eine Visitenkarte und eine Landing-Page hinzu, vielleicht auch noch Briefpapier.
Auf dem Flyer sollte ein passender/moderner (kann auch ein doppeldeutig-witziger) Slogan stehen.
(leider habe ich 'Jedes Leben ist der Rede wert' bei einem Kollegen gesehen, somit scheidet das aus, schade!)
Sicherlich lässt sich etwas ähnliches finden.
Weitere kurze Texte reiche ich nach, nur Aufzählungen von Dienstleistungen oder Schlagwörter, kein Fließtext.
Meine Kontaktdaten sollten auf die Rückseite des Flyers.

```html
<!DOCTYPE html>
<html lang="de">
<head>
<meta charset="utf-8">
<title>lichtwerk.berlin – Flyer Trauerredner</title>
<link rel="stylesheet" href="https://fonts.googleapis.com/css2?family=Tinos&display=swap">
<style>
  :root {
    --paper: #ffffff;
    --ink: #111111;
    --slogan-red: #c42420;
    --frame-berry: #b8004a;
    --frame-edge: #6a3a7a;
    --photo-dark: #050805;
    --photo-red: #8e0c04;
  }
  * { margin: 0; padding: 0; box-sizing: border-box; }
  html, body { width: 1096px; height: 1200px; overflow: hidden; background: var(--paper); }
  .flyer {
    position: relative;
    width: 1096px;
    height: 1200px;
    font-family: "Tinos", "Times New Roman", serif;
    color: var(--ink);
  }
  .brand-name {
    position: absolute;
    left: 605px; width: 470px; top: 44px;
    text-align: center;
    font-size: 32px;
    line-height: 40px;
    font-weight: 400;
    color: var(--ink);
  }
  .intro {
    position: absolute;
    left: 30px; width: 560px; top: 96px;
    text-align: center;
    font-size: 21.5px;
    line-height: 28px;
  }
  .contact {
    position: absolute;
    left: 54px; top: 346px;
    list-style: none;
    font-size: 21.5px;
  }
  .contact li { height: 83.5px; line-height: 30px; }
  .heart {
    position: absolute;
    left: 197px; top: 760px;
    width: 158px; height: 143px;
  }
  .photo-frame {
    position: absolute;
    left: 605px; top: 174px;
    width: 470px; height: 454px;
    background: var(--frame-berry);
    border: 1px solid var(--frame-edge);
  }
  .photo {
    position: absolute;
    left: 26px; top: 39px;
    width: 419px; height: 387px;
    background:
      radial-gradient(ellipse 42% 40% at 58% 45%, var(--photo-red) 0%, #5a0804 55%, rgba(5,8,5,0) 100%),
      var(--photo-dark);
  }
  .slogan {
    position: absolute;
    left: 605px; width: 432px; top: 666px;
    text-align: center;
    font-size: 36px;
    line-height: 48px;
    color: var(--slogan-red);
  }
</style>
</head>
<body>
<main class="flyer">
  <div class="brand-name">lichtwerk.berlin</div>

  <p class="intro">
    Bitte wenden Sie sich bei allen Fragen und<br>
    Wünschen, die den Ablauf und Umfang Ihrer<br>
    Trauerfeier betreffen vertrauensvoll an mich. Ich<br>
    garantiere Ihnen bei allem<br>
    meine vollste Diskretion und Verschwiegenheit.
  </p>

  <ul class="contact">
    <li>Meine Kontaktdaten lauten:</li>
    <li>Adresse</li>
    <li>Telefonnummer</li>
    <li>Website: www.lichtwerk.berlin.de</li>
    <li>QR-Code</li>
  </ul>

  <svg class="heart" viewBox="0 0 264 240" aria-hidden="true">
    <path d="M132 34 C110 0 60 -5 25 25 C-10 60 5 100 40 125 C80 150 120 165 132 238 C144 165 184 150 224 125 C259 100 274 60 239 25 C204 -5 154 0 132 34 Z"
          fill="var(--frame-berry)" stroke="var(--frame-edge)" stroke-width="1.5"/>
  </svg>

  <div class="photo-frame">
    <div class="photo" role="img" aria-label="Foto einer roten Mohnblüte vor dunklem Hintergrund"></div>
  </div>

  <p class="slogan">Viel schöner ist’s,<br>über’s Leben zu reden!</p>
</main>
</body>
</html>
```